Kolna Thai Massage Double Sided Flyer Luxury

I require a double sided flyer
we are a Thai Massage Spa
Would like gold, deep purple and bronze colours
Something eye catching and looks professional

```html
<!DOCTYPE html>
<html lang="en">
<head>
<meta charset="utf-8">
<title>Kolna Thai Massage – Flyer</title>
<link rel="stylesheet" href="https://fonts.googleapis.com/css2?family=Cinzel:wght@700&family=Gabriela&family=Marcellus&family=Montserrat:wght@500&family=Roboto+Slab:wght@500&family=Lato:ital,wght@1,700&display=swap">
<style>
  :root {
    --deep-purple: #14008a;
    --deep-purple-shade: #0c0070;
    --violet: #6c3cff;
    --violet-edge: #6a26ff;
    --gold: #ffc629;
    --white: #ffffff;
    --gap: #ffffff;
  }
  * { margin: 0; padding: 0; box-sizing: border-box; }
  html, body { width: 1200px; height: 839px; overflow: hidden; background: var(--gap); }
  .flyer { position: relative; width: 1200px; height: 839px; }

  /* Front side */
  .front {
    position: absolute; left: 0; top: 0; width: 600px; height: 839px;
    background: linear-gradient(200deg, var(--deep-purple-shade) 0%, var(--deep-purple) 30%, var(--deep-purple) 80%, var(--deep-purple-shade) 100%);
  }
  .brand-ring {
    position: absolute; left: 218px; top: 270px; width: 152px; height: 152px;
    border: 6px solid var(--gold); border-radius: 50%;
  }
  .brand-name {
    position: absolute; left: 0; width: 600px; top: 414px; text-align: center;
    font-family: "Marcellus", serif; font-size: 33px; color: var(--gold);
  }
  .contact { position: absolute; left: 50px; }
  .contact-icon { position: absolute; left: 0; width: 28px; height: 28px; fill: var(--gold); }
  .contact-text {
    position: absolute; left: 44px; white-space: nowrap;
    font-family: "Montserrat", sans-serif; font-weight: 500; font-size: 10.5px;
    letter-spacing: 1px; line-height: 16px; color: var(--gold);
  }

  /* Back side */
  .back {
    position: absolute; left: 610px; top: 0; width: 590px; height: 836px;
    background: linear-gradient(90deg, var(--violet) 0%, var(--violet) 70%, var(--violet-edge) 100%);
  }
  .headline {
    position: absolute; left: 83px; top: 80px;
    font-family: "Cinzel", serif; font-weight: 700; font-size: 45px;
    line-height: 47px; letter-spacing: 4px; color: var(--gold);
  }
  .intro {
    position: absolute; left: 83px; top: 209px; width: 426px;
    font-family: "Gabriela", serif; font-size: 15.5px; line-height: 24.7px;
    letter-spacing: 0.6px; text-align: justify; color: var(--white);
  }
  .menu-title {
    position: absolute; left: 0; width: 590px; top: 443px; text-align: center; padding-left: 30px;
    font-family: "Gabriela", serif; font-size: 13px; letter-spacing: 9px; color: var(--gold);
  }
  .menu { position: absolute; left: 171px; top: 475px; width: 245px; }
  .menu-item { border-top: 1px solid var(--gold); padding: 11px 0 10px; }
  .menu-item:last-child { border-bottom: 1px solid var(--gold); }
  .item-head {
    font-family: "Gabriela", serif; font-size: 11px; color: var(--gold);
    text-transform: uppercase; white-space: nowrap;
  }
  .item-price { font-size: 17px; margin-left: 8px; }
  .item-detail {
    list-style: none; margin-top: 3px;
    font-family: "Roboto Slab", serif; font-weight: 500; font-size: 9px;
    line-height: 14px; letter-spacing: 0.5px; color: var(--white); white-space: nowrap;
  }
  .item-detail li { padding-left: 9px; position: relative; }
  .item-detail li::before {
    content: ""; position: absolute; left: 0; top: 5px; width: 4px; height: 4px; background: var(--white);
  }
  .gift-icon { position: absolute; left: 273px; top: 716px; width: 42px; height: 40px; }
  .gift-note {
    position: absolute; left: 0; width: 590px; top: 760px; text-align: center; padding-left: 10px;
    font-family: "Lato", sans-serif; font-style: italic; font-weight: 700; font-size: 16.5px;
    letter-spacing: 1px; color: var(--white);
  }
  .gift-note em { font-style: italic; color: var(--gold); }
</style>
</head>
<body>
<main class="flyer">
  <section class="front">
    <div class="brand-ring"></div>
    <h1 class="brand-name">Kolna Thai Massage</h1>

    <div class="contact" style="top:587px">
      <svg class="contact-icon" viewBox="0 0 24 24" style="top:0"><path d="M12 1a8 8 0 0 0-8 8c0 6 8 14 8 14s8-8 8-14a8 8 0 0 0-8-8zm0 11a3 3 0 1 1 0-6 3 3 0 0 1 0 6z"/></svg>
      <p class="contact-text" style="top:0">KOLNA THAI MASSAGE<br>12 ORCHARD ROW, HARLOW BRIDGE, HB4 2QT</p>
    </div>
    <div class="contact" style="top:646px">
      <svg class="contact-icon" viewBox="0 0 24 24" style="top:0"><path d="M6.6 10.8a15.1 15.1 0 0 0 6.6 6.6l2.2-2.2c.3-.3.7-.4 1-.2 1.1.4 2.3.6 3.6.6.6 0 1 .4 1 1V20c0 .6-.4 1-1 1A17 17 0 0 1 3 4c0-.6.4-1 1-1h3.5c.6 0 1 .4 1 1 0 1.3.2 2.5.6 3.6.1.3 0 .7-.2 1z"/></svg>
      <p class="contact-text" style="top:6px">0120 5550147</p>
    </div>
    <div class="contact" style="top:703px">
      <svg class="contact-icon" viewBox="0 0 24 24" style="top:0"><circle cx="12" cy="12" r="10" fill="none" stroke="#ffc629" stroke-width="2"/><ellipse cx="12" cy="12" rx="4.5" ry="10" fill="none" stroke="#ffc629" stroke-width="2"/><path d="M2 12h20M4 7h16M4 17h16M12 2v20" stroke="#ffc629" stroke-width="2"/></svg>
      <p class="contact-text" style="top:6px">KOLNASPA.COM</p>
    </div>
    <div class="contact" style="top:760px">
      <svg class="contact-icon" viewBox="0 0 24 24" style="top:0"><path d="M2 4h20v16H2z"/><path d="M2 4l10 9 10-9M2 20l7.5-8M22 20l-7.5-8" fill="none" stroke="#14008a" stroke-width="1.5"/></svg>
      <p class="contact-text" style="top:6px">WWW.KOLNATHAIMASSAGE.CO.UK</p>
    </div>
  </section>

  <section class="back">
    <h2 class="headline">WELCOME<br>TO LUXURY</h2>
    <p class="intro">Set in the heart of Brackenhay, Kolna Thai Massage will allow you to immerse yourself in a place where your wellbeing and rejuvenation is at the centre of what we do.<br>Using Thai traditions, our highly trained therapists offer revitalising body treatments with their deep tissue massage techniques. In their hands, you will see and feel immediate results.</p>

    <h3 class="menu-title">MASSAGES</h3>
    <div class="menu">
      <div class="menu-item">
        <p class="item-head">Deep Tissue Massage <span class="item-price">£45</span></p>
        <ul class="item-detail"><li>60 minutes</li><li>Oil Massage Personalised, Light To Firm Pressure</li></ul>
      </div>
      <div class="menu-item">
        <p class="item-head">Deep Tissue Massage <span class="item-price">£55</span></p>
        <ul class="item-detail"><li>90 minutes</li><li>Oil Massage, Medium To Firm Pressure</li></ul>
      </div>
      <div class="menu-item">
        <p class="item-head">Thai Floor Tradtional Massage <span class="item-price">£45</span></p>
        <ul class="item-detail"><li>60 minutes</li><li>Dry massage, medium to firm pressure applying<br>stretching technique</li></ul>
      </div>
    </div>

    <svg class="gift-icon" viewBox="0 0 42 40" aria-hidden="true">
      <path d="M21 37C8 28 3 21 3 13a9 9 0 0 1 18-3 9 9 0 0 1 18 3c0 8-5 15-18 24z" fill="#ffc629"/>
      <path d="M21 2v38M1 18h40" stroke="#ffffff" stroke-width="1.6"/>
    </svg>
    <p class="gift-note">GIFT <em>VOUCHERS</em> AVAILABLE</p>
  </section>
</main>
</body>
</html>
```